sign business needs card design

I need a very clean design for my business card.
It is a sign company. Banners By Noon is the name of the business.
Our colors are orange, yellow. But I want a very professional card.
But you can use any colors. I like a black background with orange letters or a white back with a clean look. No cartoon or kiddy looking print. The info. I need on the card is as follows.
Banners By Noon
318.555.0172 ph.
318.555.0199 fax.
email.bannersbynoon@mailvista.net
web.bannersbynooninc.com
4187 N. Maplecrest Lane Ste. 2b
Dale Hutchins

```html
<!DOCTYPE html>
<html lang="en">
<head>
<meta charset="utf-8">
<title>Banners By Noon – Business Card</title>
<link rel="stylesheet" href="https://fonts.googleapis.com/css2?family=Jost:wght@300&family=Arimo:wght@400&display=swap">
<style>
  :root {
    --orange: #e67a26;
    --ink-orange: #e6812f;
    --paper: #ffffff;
    --trim: #a9d4ea;
  }
  * { margin: 0; padding: 0; box-sizing: border-box; }
  html, body {
    width: 1200px;
    height: 741px;
    overflow: hidden;
    background: var(--paper);
  }
  .card {
    position: relative;
    width: 1200px;
    height: 741px;
    background: var(--paper);
    font-family: "Arimo", Arial, sans-serif;
    color: var(--ink-orange);
  }
  .trim-line {
    position: absolute;
    left: 0;
    width: 1200px;
    height: 2px;
    background: var(--trim);
  }
  .trim-line--top { top: 6px; }
  .trim-line--bottom { top: 737px; }

  .name-band {
    position: absolute;
    left: 38px;
    top: 235px;
    width: 659px;
    height: 195px;
    background: var(--orange);
    color: var(--paper);
    text-align: center;
  }
  .company-name {
    position: absolute;
    left: 0;
    right: 0;
    top: 30px;
    font-family: "Jost", "Futura", sans-serif;
    font-weight: 300;
    font-size: 66px;
    line-height: 1;
    font-variant: small-caps;
    letter-spacing: 0.5px;
  }
  .person-name {
    position: absolute;
    left: 0;
    right: 0;
    top: 115px;
    font-size: 35px;
    line-height: 1;
  }
  .accent-bar {
    position: absolute;
    left: 1135px;
    top: 237px;
    width: 35px;
    height: 193px;
    background: var(--orange);
  }

  .address,
  .contact-line {
    position: absolute;
    white-space: nowrap;
    line-height: 1;
  }
  .address { left: 70px; top: 481px; font-size: 36px; }
  .contact-line { font-size: 33px; }
  .email { left: 70px; top: 566px; }
  .website { left: 70px; top: 612px; }
  .phone { left: 527px; top: 564px; }
  .fax { left: 527px; top: 617px; }
  .fax .number { position: absolute; left: 111px; }
</style>
</head>
<body>
  <main class="card">
    <div class="trim-line trim-line--top"></div>
    <div class="trim-line trim-line--bottom"></div>

    <section class="name-band">
      <h1 class="company-name">Banners By Noon</h1>
      <p class="person-name">Dale Hutchins</p>
    </section>
    <div class="accent-bar"></div>

    <p class="address">4187 N. Maplecrest Lane Ste. 2b</p>
    <p class="contact-line email">bannersbynoon@mailvista.net</p>
    <p class="contact-line website">www.bannersbynooninc.com</p>
    <p class="contact-line phone">Phone: 318.555.0172</p>
    <p class="contact-line fax">Fax:<span class="number">318.555.0199</span></p>
  </main>
</body>
</html>
```